Personal Blog

The wordpress blog style and layout should be similar to http://www.ninalofwent.com

homepage: my photo, list of things, call to action then 3 boxes (The Blog, The Book and podcast)

Other pages: About us, Blog, Consulting, Contact

Target Market(s)

Web Marketing Consultant

Industry/Entity Type

Consulting

Colors
3277b5
33a6d7
f04a50
f68e4e
33b7a4

```html
<!DOCTYPE html>
<html lang="en">
<head>
<meta charset="utf-8">
<title>Blogger Name – Personal Blog</title>
<link href="https://fonts.googleapis.com/css2?family=Oswald:wght@300;400&display=swap" rel="stylesheet">
<style>
:root{
  --orange:#f68e4e;
  --dark:#4a4a4a;
  --ink:#4d4d4d;
  --paper:#f3f3f3;
  --white:#ffffff;
  --line:#e2e2e2;
  --fb:#3277b5;
}
*{margin:0;padding:0;box-sizing:border-box}
html,body{width:998px;height:1200px;overflow:hidden;background:var(--paper)}
body{font-family:Arial,Helvetica,sans-serif;color:var(--ink)}
.page{position:relative;width:998px;height:1200px;overflow:hidden}
.abs{position:absolute}
.display{font-family:"Oswald",sans-serif;font-weight:300;text-transform:uppercase;letter-spacing:-.2px}

/* header */
.site-header{left:0;top:0;width:998px;height:104px;background:repeating-linear-gradient(90deg,#4c4c4c 0 2px,#474747 2px 4px);border-bottom:3px solid #d9d9d9}
.brand{left:81px;top:20px;display:flex;align-items:center;gap:10px}
.brand-square{width:50px;height:50px;background:var(--orange);border-radius:6px}
.brand-name{font-family:"Oswald",sans-serif;font-weight:400;font-size:30px;line-height:1;color:var(--white)}
.main-nav{top:38px;left:0;width:998px;height:24px}
.main-nav a{position:absolute;font-family:"Oswald",sans-serif;font-weight:300;font-size:16px;color:var(--white);text-decoration:none;text-transform:uppercase}
.main-nav a.current{color:var(--orange)}

/* headline band */
.headline-band{left:0;top:107px;width:998px;height:77px;background:#f0f0f0;border-bottom:2px solid var(--white);text-align:center}
.headline-band h1{font-size:31px;color:#444;margin-top:4px;line-height:1.25}
.headline-band h1 span{color:var(--orange)}
.headline-band p{font-size:17px;color:#555;line-height:1.2}

/* hero */
.hero{left:0;top:186px;width:998px;height:209px;background:#ececec}
.hero-photo{left:69px;top:0;width:390px;height:209px;background:linear-gradient(90deg,#dcdcdc 0%,#cfd6df 40%,#e4e9f0 70%,#ececec 100%)}
.benefits{left:486px;top:26px;list-style:none}
.benefits li{font-size:12.5px;color:#444;height:26px;padding-left:16px;position:relative}
.benefits li::before{content:"";position:absolute;left:0;top:3px;width:5px;height:5px;border-right:2px solid var(--orange);border-top:2px solid var(--orange);transform:rotate(45deg)}

/* featured */
.featured{left:0;top:395px;width:998px;height:87px;background:var(--white)}
.featured-label{left:93px;top:25px;font-family:"Oswald",sans-serif;font-weight:300;font-size:20px;color:var(--orange)}
.featured-chevron{left:203px;top:0}
.press-row{left:251px;top:28px;display:flex;gap:14px;align-items:center}
.press-badge{width:80px;height:26px;background:#d6d6d6;border-radius:3px}

/* intro */
.intro{left:127px;top:492px;width:760px;font-size:20px;letter-spacing:-.6px;line-height:28px;color:#555}
.intro span{color:#9a9a9a}

/* cards */
.card{top:630px;width:276px;height:250px;background:var(--white);border:1px solid var(--line);border-top:4px solid var(--orange);text-align:center}
.card-photo{position:absolute;left:46px;top:-75px;width:180px;height:180px;border-radius:50%;border:4px solid var(--white);box-shadow:0 0 0 1px #ddd}
.card h2{position:absolute;top:108px;left:0;width:100%;font-size:22px;color:var(--orange)}
.card p{position:absolute;top:143px;left:8px;width:260px;text-align:left;font-size:11.3px;line-height:19px;color:#444}
.card .btn{position:absolute;top:202px;left:89px;width:90px;height:30px;background:var(--dark);border:2px solid var(--white);box-shadow:0 0 0 1px var(--dark);color:var(--white);font-family:"Oswald",sans-serif;font-size:15px;line-height:26px;text-decoration:none}

/* footer */
.site-footer{left:0;top:909px;width:998px;height:291px;background:repeating-linear-gradient(90deg,#4a4a4a 0 2px,#454545 2px 4px);border-top:3px solid #d0d0d0;color:var(--white)}
.site-footer h3{font-size:21px;line-height:26px;color:var(--white)}
.site-footer p{font-size:11px;line-height:15px;color:#eee}
.bio-photo{left:79px;top:69px;width:86px;height:86px;background:linear-gradient(180deg,#d9dde3,#bfc6cf)}
.footer-link{font-family:"Oswald",sans-serif;font-weight:300;font-size:14px;color:var(--orange)}
.field{width:250px;height:26px;background:var(--white);font-size:11px;color:#999;padding-left:7px;line-height:26px}
.join-btn{width:250px;height:28px;background:var(--orange);border:1px solid #e07e3f;color:var(--white);font-family:"Oswald",sans-serif;font-weight:300;font-size:17px;text-align:center;line-height:26px;text-transform:uppercase}
.pb-square{left:665px;top:67px;width:38px;height:38px;background:var(--fb);border-radius:4px;border:2px solid var(--white)}
.social{width:39px;height:39px;border-radius:50%;border:2px solid var(--orange);display:flex;align-items:center;justify-content:center;font-family:"Oswald",sans-serif;font-weight:400;font-size:17px;color:var(--white)}
.social.active{background:var(--orange);border-color:#e8e8e8}
.footer-rule{left:64px;top:255px;width:870px;height:1px;background:#666}
.copyright{left:0;top:266px;width:998px;text-align:center;font-size:11px;color:#eee}
</style>
</head>
<body>
<div class="page">

<header class="site-header abs">
  <div class="brand abs"><span class="brand-square"></span><span class="brand-name">Blogger Name</span></div>
  <nav class="main-nav abs">
    <a class="current" style="left:431px">About</a>
    <a style="left:509px">Blog</a>
    <a style="left:580px">Consulting</a>
    <a style="left:693px">Podcast</a>
    <a style="left:785px">Book</a>
    <a style="left:856px">Contact</a>
  </nav>
</header>

<section class="headline-band abs">
  <h1 class="display">Join my <span>new business bootcamp</span> for free!</h1>
  <p class="display">I'll show you how to start, run, &amp; grow a business in the 21st century</p>
</section>

<section class="hero abs">
  <div class="hero-photo abs" role="img" aria-label="Smiling man in a shirt and red tie seated beside a computer monitor"></div>
  <ul class="benefits abs">
    <li>Apply Smart Social Media Strategies</li>
    <li>Create Raving Fans with Free eBooks</li>
    <li>Utilize the Power of Blogging for Business</li>
    <li>Grow Your Empire Through Outsourcing</li>
    <li>Attract Customers with Videos &amp; Podcasts</li>
    <li>Plus, Much More!</li>
  </ul>
</section>

<section class="featured abs">
  <div class="featured-label abs">As Featured In:</div>
  <svg class="featured-chevron abs" width="32" height="87" viewBox="0 0 32 87"><polyline points="2,0 28,43 2,87" fill="none" stroke="#f68e4e" stroke-width="5"/></svg>
  <div class="press-row abs">
    <div class="press-badge"></div><div class="press-badge" style="width:56px"></div><div class="press-badge" style="width:70px"></div><div class="press-badge" style="width:60px"></div><div class="press-badge" style="width:64px"></div><div class="press-badge" style="width:66px"></div><div class="press-badge" style="width:72px"></div><div class="press-badge" style="width:70px"></div>
  </div>
</section>

<p class="intro display abs">Lorem Ipsum is simply dummy text of the printing and typesetting industry. Lorem Ipsum has been the industry's standard… <span>dummy text ever since the 1500s</span></p>

<article class="card abs" style="left:67px">
  <div class="card-photo" role="img" aria-label="Businessman in a suit working on a laptop" style="background:linear-gradient(160deg,#d8d8d8,#6d6d6d)"></div>
  <h2 class="display">The Blog</h2>
  <p>Lorem Ipsum is simply dummy text of the printing and typesetting industry. Lorem Ipsum has been the industry's standard dummy text ever!</p>
  <a class="btn">Learn More</a>
</article>
<article class="card abs" style="left:361px">
  <div class="card-photo" role="img" aria-label="Blue molecular model in front of laboratory glassware" style="background:radial-gradient(circle,#cfe6fa,#3a8ad6)"></div>
  <h2 class="display">The Book</h2>
  <p>Lorem Ipsum is simply dummy text of the printing and typesetting industry. Lorem Ipsum has been the industry's</p>
  <a class="btn">Learn More</a>
</article>
<article class="card abs" style="left:656px">
  <div class="card-photo" role="img" aria-label="Businessman in a grey suit in a meeting room" style="background:linear-gradient(160deg,#e9e4dc,#a89a86)"></div>
  <h2 class="display">The Podcast</h2>
  <p>Lorem Ipsum is simply dummy text of the printing and typesetting industry. Lorem Ipsum has been the industry's standard dummy text ever!</p>
  <a class="btn">Learn More</a>
</article>

<footer class="site-footer abs">
  <h3 class="display abs" style="left:76px;top:8px">Entrepreneur, Speaker,<br>Consultant and more!</h3>
  <div class="bio-photo abs" role="img" aria-label="Portrait of the blogger"></div>
  <p class="abs" style="left:176px;top:69px;width:155px">Lorem Ipsum is simply dummy text of the printing and typesetting industry. Lorem Ipsum has been the industry's standard dummy text ever Lorem Ipsum is simply dummy</p>
  <p class="abs" style="left:76px;top:169px;width:260px">since the 1500s, when an unknown printer took a galley of type and scrambled it to make a type specimen book.</p>
  <div class="footer-link abs" style="left:118px;top:218px">Read the long-winded version!</div>

  <h3 class="display abs" style="left:369px;top:8px">Join my new business<br>bootcamp for free!</h3>
  <p class="abs" style="left:371px;top:62px;width:250px;line-height:19px">Lorem Ipsum is simply dummy text of the printing and typesetting industry. Lorem Ipsum has been the industry's standard dummy text ever</p>
  <div class="field abs" style="left:371px;top:124px">Enter your name</div>
  <div class="field abs" style="left:371px;top:167px">Enter your name</div>
  <div class="join-btn abs" style="left:371px;top:211px">Join for free!</div>

  <h3 class="display abs" style="left:666px;top:8px">Become part of my rockin'<br>Pagebook community</h3>
  <div class="pb-square abs"></div>
  <p class="abs" style="left:712px;top:67px;width:210px">Lorem Ipsum is simply dummy text of the printing and typesetting industry. Lorem Ipsum has been the industry's standard.</p>
  <h3 class="display abs" style="left:666px;top:115px">Connect with me</h3>
  <div class="social active abs" style="left:667px;top:150px" aria-label="Pagebook">P</div>
  <div class="social abs" style="left:735px;top:150px" aria-label="Chirper">C</div>
  <div class="social abs" style="left:804px;top:150px" aria-label="Searchly">S</div>
  <div class="social abs" style="left:667px;top:203px" aria-label="ViewTube">V</div>
  <div class="social abs" style="left:735px;top:203px" aria-label="Feed">
    <svg width="18" height="18" viewBox="0 0 18 18" fill="none" stroke="#fff" stroke-width="2.4"><circle cx="3" cy="15" r="1.6" fill="#fff" stroke="none"/><path d="M2 8a8 8 0 0 1 8 8"/><path d="M2 2a14 14 0 0 1 14 14"/></svg>
  </div>
  <div class="social abs" style="left:804px;top:203px" aria-label="Email">
    <svg width="20" height="14" viewBox="0 0 20 14"><rect x="0" y="0" width="20" height="14" rx="2" fill="#fff"/><polyline points="1,1 10,8 19,1" fill="none" stroke="#4a4a4a" stroke-width="1.6"/></svg>
  </div>

  <div class="footer-rule abs"></div>
  <div class="copyright abs">© BLOGGER NAME - 2014. All Rights Reserved.</div>
</footer>

</div>
</body>
</html>
```